Quillfern Nightclub Flyer (Updated)

Flyer for facebook, square is fine, or rectangular. Here is the text:
QUILLFERN
Nightclub + Lounge
presents

SPLIT DECK WEDNESDAY
Nov 29 2018

CLUB FLOOR:
GORDY B2B RALPH
THEODORE BRUSKVIK

LOUNGE:
OTIS B2B HALF TIDE
COPPER FENWICK

Powered by HALVERN Acoustics
4716 Larchmere Avenue 21+ 9pm-2am
quillfernvenue-example.com for VIP booth inquiries

Target Market(s)

Nightclub

Industry/Entity Type

Night Club

Font styles to use
Sans Serif

Colors

Designer to choose colors to be used in the design.

Requirements
Must have
• All the text listed, and plz keep the theme of the attached files. We want to stay consistent with the Quillfern brand
Nice to have
• Try to stay with the theme from the attachments
Should not have
• Dont' stray to far from the general theme we have from the attachments

```html
<!DOCTYPE html>
<html lang="en">
<head>
<meta charset="utf-8">
<title>Quillfern Nightclub + Lounge — Split Deck Wednesday</title>
<link rel="stylesheet" href="https://fonts.googleapis.com/css2?family=Lato:wght@400;700&display=swap">
<style>
  :root {
    --paper: #f1eee9;
    --paper-light: #fbfaf8;
    --ink: #1c1c1c;
    --ink-soft: #5e5e5e;
    --gold: #d6a04c;
    --gold-pale: #ead7b4;
    --gold-mist: #f3e6cf;
  }
  * { margin: 0; padding: 0; box-sizing: border-box; }
  html, body { width: 1160px; height: 1200px; overflow: hidden; background: var(--paper); }
  body { font-family: "Lato", sans-serif; color: var(--ink); }

  .flyer { position: relative; width: 1160px; height: 1200px; overflow: hidden; }

  .damask-field {
    position: absolute; inset: 0;
    background: radial-gradient(ellipse 520px 560px at 580px 520px, var(--paper-light) 0%, var(--paper) 100%);
  }
  .mandala-corner {
    position: absolute; left: -300px; top: 610px;
    width: 640px; height: 640px; border-radius: 50%;
    background: radial-gradient(circle at center, var(--gold-pale) 0%, var(--gold-mist) 55%, rgba(243,230,207,0) 72%);
  }
  .frames { position: absolute; inset: 0; }

  .line { position: absolute; left: 0; width: 100%; text-align: center; white-space: nowrap; }

  .brand-seal {
    position: absolute; left: 501px; top: 137px;
    width: 158px; height: 158px; border-radius: 50%;
    background: var(--gold);
  }
  .brand-name { top: 330px; font-size: 68px; font-weight: 400; letter-spacing: 6px; line-height: 80px; }
  .brand-tagline { top: 412px; font-size: 18px; letter-spacing: 3.4px; color: var(--ink-soft); line-height: 22px; }
  .presents { top: 464px; font-size: 29px; color: var(--ink-soft); line-height: 34px; }

  .event-title, .event-date, .slot-line { font-size: 27px; line-height: 36px; }
  .event-title { top: 533px; }
  .event-date { top: 569px; }

  .divider {
    position: absolute; left: 405px; width: 370px; height: 2px;
    background: linear-gradient(90deg, rgba(214,160,76,0) 0%, var(--gold) 50%, rgba(214,160,76,0) 100%);
  }
  .divider--event { top: 625px; }
  .divider--rooms { top: 768px; }
  .divider--footer { top: 1009px; left: 300px; width: 600px; opacity: 0.5; }

  .club-floor .slot-line:nth-child(1) { top: 644px; }
  .club-floor .slot-line:nth-child(2) { top: 680px; }
  .club-floor .slot-line:nth-child(3) { top: 716px; }
  .lounge .slot-line:nth-child(1) { top: 779px; }
  .lounge .slot-line:nth-child(2) { top: 815px; }
  .lounge .slot-line:nth-child(3) { top: 851px; }

  .sponsor { top: 940px; font-size: 27px; color: var(--ink); line-height: 40px; }
  .sponsor .sponsor-name { font-weight: 700; font-size: 36px; letter-spacing: 2px; margin: 0 14px; vertical-align: -2px; }

  .venue-details { top: 1016px; font-size: 28px; color: #333; line-height: 36px; }
  .venue-web { top: 1057px; font-size: 30px; color: #333; line-height: 38px; }
</style>
</head>
<body>
<main class="flyer">
  <div class="damask-field" role="img" aria-label="Soft ivory damask floral pattern background"></div>
  <div class="mandala-corner" role="img" aria-label="Gold mandala ornament rising from the lower left corner"></div>

  <svg class="frames" width="1160" height="1200" viewBox="0 0 1160 1200" aria-hidden="true">
    <path d="M102 61 H1058 A62 62 0 0 0 1120 123 V1079 A62 62 0 0 0 1058 1141 H102 A62 62 0 0 0 40 1079 V123 A62 62 0 0 0 102 61 Z"
          fill="none" stroke="var(--gold)" stroke-width="5"/>
    <rect x="69" y="89" width="1022" height="1023" fill="none" stroke="var(--ink)" stroke-width="2"/>
  </svg>

  <header class="brand">
    <div class="brand-seal" aria-hidden="true"></div>
    <h1 class="line brand-name">QUILLFERN</h1>
    <p class="line brand-tagline">NIGHTCLUB + LOUNGE</p>
    <p class="line presents">presents</p>
  </header>

  <section class="event">
    <h2 class="line event-title" style="font-weight:400">SPLIT DECK WEDNESDAY</h2>
    <p class="line event-date">Nov 29 2018</p>
  </section>

  <div class="divider divider--event"></div>

  <section class="club-floor">
    <p class="line slot-line">CLUB FLOOR:</p>
    <p class="line slot-line">GORDY B2B RALPH</p>
    <p class="line slot-line">THEODORE BRUSKVIK</p>
  </section>

  <div class="divider divider--rooms"></div>

  <section class="lounge">
    <p class="line slot-line">LOUNGE:</p>
    <p class="line slot-line">OTIS B2B HALF TIDE</p>
    <p class="line slot-line">COPPER FENWICK</p>
  </section>

  <footer>
    <p class="line sponsor">Powered by<span class="sponsor-name">HALVERN</span>Acoustics</p>
    <div class="divider divider--footer"></div>
    <p class="line venue-details">4716 Larchmere Avenue 21+ 9pm-2am</p>
    <p class="line venue-web">quillfernvenue-example.com for VIP booth inquiries</p>
  </footer>
</main>
</body>
</html>
```